VentriLedger.Com PowerPoint

I need a PowerPoint layout for my presentations. My business is called VentriLedger.Com - my presentations teach cardiologists how to document their procedures and visits and teaches them how to bill accurately for them.

Industry/Entity Type

Business

Requirements
Must have
• the logo should be subtly there on each page - perhaps as a watermark? I'm really not creative; please help.

```html
<!DOCTYPE html>
<html lang="en">
<head>
<meta charset="utf-8">
<title>VentriLedger.Com – Title Slide</title>
<link href="https://fonts.googleapis.com/css2?family=Archivo+Black&family=Roboto:wght@400;500&display=swap" rel="stylesheet">
<style>
  :root {
    --canvas: #ffffff;
    --ink: #333333;
    --ink-soft: #3a3a3a;
    --brand-red: #c01e25;
    --heart-tone-a: #d9534f;
    --heart-tone-b: #c0393a;
    --pulse-tone: #f4f4f4;
    --footer-text: #ffffff;
  }
  * { margin: 0; padding: 0; box-sizing: border-box; }
  html, body {
    width: 1200px;
    height: 900px;
    overflow: hidden;
    background: var(--canvas);
  }
  .slide {
    position: relative;
    width: 1200px;
    height: 900px;
    background: var(--canvas);
    font-family: "Roboto", Arial, sans-serif;
    color: var(--ink);
  }
  .pulse-band {
    position: absolute;
    left: 0;
    top: 352px;
    width: 960px;
    height: 226px;
    background: linear-gradient(90deg, var(--pulse-tone) 0%, var(--pulse-tone) 70%, rgba(244,244,244,0) 100%);
  }
  .heart-illustration {
    position: absolute;
    left: 82px;
    top: 180px;
    width: 256px;
    height: 445px;
    border-radius: 8px;
    background: linear-gradient(180deg, var(--heart-tone-a) 0%, var(--heart-tone-b) 100%);
  }
  .brand-name {
    position: absolute;
    right: 36px;
    top: 318px;
    display: flex;
    align-items: center;
    gap: 14px;
    font-weight: 500;
    font-size: 44px;
    line-height: 52px;
    color: var(--ink);
    letter-spacing: 0.5px;
  }
  .brand-dot {
    width: 30px;
    height: 30px;
    border-radius: 50%;
    background: var(--brand-red);
  }
  .project-title {
    position: absolute;
    right: 36px;
    top: 434px;
    font-family: "Archivo Black", "Arial Black", sans-serif;
    font-weight: 400;
    font-size: 38px;
    line-height: 48px;
    color: var(--ink);
    text-align: right;
    white-space: nowrap;
  }
  .project-summary {
    position: absolute;
    right: 36px;
    top: 493px;
    text-align: right;
    font-size: 26px;
    line-height: 37.5px;
    letter-spacing: 0.2px;
    color: var(--ink);
    white-space: nowrap;
  }
  .footer-band {
    position: absolute;
    left: 0;
    bottom: 0;
    width: 1200px;
    height: 83px;
    background: var(--brand-red);
  }
  .copyright {
    position: absolute;
    right: 0;
    top: 19px;
    width: 291px;
    height: 43px;
    background: var(--ink-soft);
    border-radius: 10px 0 0 10px;
    color: var(--footer-text);
    font-size: 21px;
    line-height: 43px;
    text-align: center;
    letter-spacing: 0.3px;
  }
</style>
</head>
<body>
  <div class="slide">
    <div class="pulse-band" role="img" aria-label="Faint heartbeat trace decoration"></div>

    <div class="heart-illustration" role="img" aria-label="Illustration of a human heart"></div>

    <div class="brand-name"><span class="brand-dot"></span>VentriLedger.Com</div>

    <h1 class="project-title">PROJECT TITLE HERE</h1>

    <p class="project-summary">
      Content here, Content here<br>
      Content here Content here, Content here<br>
      Content here Content here
    </p>

    <footer class="footer-band">
      <div class="copyright">COYPRIGHT TEXT HERE</div>
    </footer>
  </div>
</body>
</html>
```